A4 Simple eye catching special offers page with minimal text

I would like an A4 page to advertise my special offers on for sale sign boards. I want my logo on the design and maybe some pictures i have attached, or maybe a design without the pictures i might like the design with or without them. The following text should be used:
Free boards
Free rebrand
Read on to find out more

Target Market(s)

Businesses

Industry/Entity Type

Real Estate Agent

Requirements
Must have
• good design
Nice to have
• eye catching

```html
<!DOCTYPE html>
<html lang="en">
<head>
<meta charset="utf-8">
<title>Boardwise – Special Offers</title>
<link rel="stylesheet" href="https://fonts.googleapis.com/css2?family=Roboto:wght@400;700;900&display=swap">
<style>
  :root {
    --navy: #2e2d52;
    --red: #e52630;
    --pink: #ff5a6a;
    --white: #ffffff;
    --mist: #e4e7e7;
    --backdrop: #d9d9dc;
  }
  * { margin: 0; padding: 0; box-sizing: border-box; }
  html, body {
    width: 1200px; height: 1196px; overflow: hidden;
    background: var(--backdrop);
    font-family: "Roboto", Arial, sans-serif;
  }
  .sheet {
    position: absolute; left: 184px; top: 13px;
    width: 903px; height: 1272px;
    background: var(--white);
    transform: scale(0.919); transform-origin: top left;
    overflow: hidden;
  }
  .sheet-art { position: absolute; inset: 0; width: 903px; height: 1272px; }
  .masthead {
    position: absolute; left: 0; top: 0; width: 903px; height: 155px;
    background: var(--navy);
  }
  .brand {
    position: absolute; left: 68px; top: 48px;
    display: flex; align-items: center; gap: 12px;
    color: var(--red); font-weight: 900; font-size: 50px; letter-spacing: -1px;
  }
  .brand-square { width: 22px; height: 22px; background: var(--red); }
  .offer {
    position: absolute; right: 67px; top: 50px; text-align: right;
    font-weight: 700; font-size: 20px; line-height: 27px;
  }
  .offer-main { color: var(--white); }
  .offer-main .slash { color: var(--red); padding: 0 6px; }
  .offer-cta { color: var(--red); }
  .web-box {
    position: absolute; left: 70px; top: 1182px; width: 253px; height: 52px;
    background: var(--navy); border: 3px solid var(--red);
    color: var(--white); font-weight: 700; font-size: 18px;
    display: flex; align-items: center; justify-content: center;
  }
  .contact {
    position: absolute; top: 1190px; right: 67px;
    display: flex; align-items: stretch;
    color: var(--navy); font-size: 13px; line-height: 17px;
  }
  .contact-address { text-align: right; }
  .contact-rule { width: 2px; background: var(--red); margin: 2px 19px; }
</style>
</head>
<body>
  <main class="sheet">
    <svg class="sheet-art" viewBox="0 0 903 1272" aria-hidden="false">
      <defs>
        <linearGradient id="signs" x1="0" y1="0" x2="1" y2="1">
          <stop offset="0" stop-color="#8a4a3a"/>
          <stop offset="0.3" stop-color="#2fa3b5"/>
          <stop offset="0.55" stop-color="#4b2a86"/>
          <stop offset="0.75" stop-color="#cfe036"/>
          <stop offset="1" stop-color="#2e2d52"/>
        </linearGradient>
      </defs>
      <rect class="hero-photo" role="img" aria-label="Photo of a row of colourful estate agent for-sale boards outside brick houses"
            x="0" y="155" width="903" height="530" fill="url(#signs)"/>
      <polygon class="hero-navy" points="640,560 903,420 903,680 760,620" fill="var(--navy)"/>
      <polygon class="hero-band" points="355,483 903,358 903,498 355,588" fill="var(--red)"/>
      <polygon class="hero-band-light" points="440,545 818,470 818,530 440,580" fill="var(--pink)" opacity="0.55"/>
      <polygon class="hero-band-light" points="700,402 903,355 903,430 700,455" fill="var(--pink)" opacity="0.6"/>
      <polygon class="hero-band-light" points="548,430 820,380 820,410 548,460" fill="var(--pink)" opacity="0.4"/>
      <polygon class="content-edge" points="0,660 621,528 903,668 903,680 621,540 0,672" fill="var(--mist)"/>
      <polygon class="content-panel" points="0,672 621,540 903,680 903,1272 0,1272" fill="var(--white)"/>
      <polygon class="foot-stripe" points="0,1091 290,1272 0,1272" fill="var(--red)"/>
      <polygon class="foot-corner" points="0,1118 212,1272 0,1272" fill="var(--navy)"/>
    </svg>

    <header class="masthead">
      <div class="brand"><span class="brand-name">Boardwise</span><span class="brand-square"></span></div>
      <div class="offer">
        <p class="offer-main">FREE BOARDS<span class="slash">/</span>FREE REBRAND</p>
        <p class="offer-cta">READ ON TO FIND OUT MORE</p>
      </div>
    </header>

    <footer>
      <div class="web-box">www.Boardwise.co.uk</div>
      <div class="contact">
        <p class="contact-address">Unit 14, Mill Lane Trade Park<br>Mill Lane, Ashford, Kent, TN24 8QP</p>
        <span class="contact-rule"></span>
        <p class="contact-lines">0300 555 0187<br>info@boardwise.co.uk</p>
      </div>
    </footer>
  </main>
</body>
</html>
```